ZEPHIRO needs a new business card!

ZEPHIRO is a group of gaming enthusiasts who are looking for a new corporate business card.

The typeface should be modern and minimalist with attention paid to spacing between the letters and the letters 'zephiro' look relative to each other.

Should clean, crisp and minimalist - looking serious overall but with slight tweaks to the letters to make them look playful...

Black on white is fine.

Details on the card should include:
-the word 'zephiro'
-a job title (use any, for e.g. founder)
-a name (e.g. Ned Falka)
-phone number
-email address

For inspiration: http://brisket.tumblevane-cdn.example/wp-content/uploads/2013/07/mela-1.jpg

Target Market(s)

Video gaming enthusiasts

Industry/Entity Type

Business

Requirements
Must have
• Black letter on white background.
The word "zephiro"
Nice to have
• Maybe use a conservative font like Gibraltar or Helvetica and tweaking each letter individually.

You can insert normal job titles under the "zephiro" typeface
Should not have
• Should not be cartoony or childish fonts. No colors.

```html
<!DOCTYPE html>
<html lang="en">
<head>
<meta charset="utf-8">
<title>ZEPHIRO — Business Card</title>
<link rel="stylesheet" href="https://fonts.googleapis.com/css2?family=Arimo:wght@400;700&display=swap">
<style>
  :root {
    --backdrop: #2b2b2b;
    --card: #ffffff;
    --ink: #000000;
  }
  html, body {
    margin: 0;
    padding: 0;
    width: 1200px;
    height: 1000px;
    overflow: hidden;
    background: var(--backdrop);
    font-family: "Arimo", Arial, sans-serif;
    color: var(--ink);
  }
  .card {
    position: absolute;
    left: 169px;
    top: 267px;
    width: 862px;
    height: 472px;
    background: var(--card);
  }
  .card__pointer {
    position: absolute;
    left: 0;
    top: 246px;
    width: 32px;
    height: 64px;
  }
  .card__wordmark {
    position: absolute;
    right: 39px;
    top: 24px;
    margin: 0;
    font-size: 72px;
    font-weight: 700;
    line-height: 1;
    letter-spacing: 3px;
  }
  .holder__name {
    position: absolute;
    left: 67px;
    top: 259px;
    margin: 0;
    font-size: 36px;
    font-weight: 700;
    line-height: 1;
    letter-spacing: 2.5px;
  }
  .holder__title {
    position: absolute;
    left: 67px;
    top: 296px;
    margin: 0;
    font-size: 16px;
    line-height: 1;
    letter-spacing: 1px;
  }
  .contact {
    position: absolute;
    top: 344px;
    margin: 0;
  }
  .contact--phone { left: 88px; }
  .contact--email { left: 284px; }
  .contact__label {
    display: block;
    font-size: 17px;
    font-weight: 700;
    line-height: 1;
    letter-spacing: 2px;
  }
  .contact__value {
    display: block;
    margin-top: 8px;
    font-size: 18px;
    line-height: 1;
    letter-spacing: 1px;
  }
</style>
</head>
<body>
  <main class="card">
    <svg class="card__pointer" viewBox="0 0 32 64" aria-hidden="true">
      <polygon points="0,0 32,32 0,64" fill="var(--ink)"/>
    </svg>
    <h1 class="card__wordmark">ZEPHIRO</h1>
    <h2 class="holder__name">NED FALKA</h2>
    <p class="holder__title">FOUNDER</p>
    <p class="contact contact--phone">
      <span class="contact__label">PHONE:</span>
      <span class="contact__value">55501987</span>
    </p>
    <p class="contact contact--email">
      <span class="contact__label">EMAIL:</span>
      <span class="contact__value">ned.falka@mailbox.test</span>
    </p>
  </main>
</body>
</html>
```